Business Card Design

We need a design for business cards for our company. We have a logo. We teach EMT's and we are based out of Virginia. The information that will need to add would be, name, title, phone number, email, address. On the back of the business card would be "We help you, help others"

Target Market(s)

People that want to become EMT's

Colors

Designer to choose colors to be used in the design.

Requirements
Must have
• company logo

```html
<!DOCTYPE html>
<html lang="en">
<head>
<meta charset="utf-8">
<title>Responder Training – Business Card</title>
<link rel="stylesheet" href="https://fonts.googleapis.com/css2?family=Figtree:wght@400;600;700;800&display=swap">
<style>
  :root {
    --backdrop: #7d6346;
    --card: #202a34;
    --accent: #e5283f;
    --muted: #7f8a94;
    --text: #e4e7ea;
    --divider: #46515b;
  }
  * { margin: 0; padding: 0; box-sizing: border-box; }
  html, body { width: 900px; height: 1200px; overflow: hidden; }
  body {
    background: var(--backdrop);
    font-family: "Figtree", Arial, sans-serif;
    position: relative;
  }
  .card {
    position: absolute;
    left: 82px;
    width: 733px;
    height: 428px;
    background: var(--card);
    border-radius: 22px;
    box-shadow: 0 6px 14px rgba(0,0,0,0.35);
  }
  .card-front { top: 138px; }
  .card-back { top: 633px; }

  .brand {
    position: absolute;
    left: 46px;
    top: 178px;
    display: flex;
    align-items: center;
    gap: 12px;
  }
  .brand-dot {
    width: 22px; height: 22px;
    border-radius: 50%;
    background: var(--accent);
    flex: none;
  }
  .brand-name {
    color: var(--accent);
    font-weight: 800;
    font-size: 29px;
    line-height: 1;
    letter-spacing: 0.5px;
    text-transform: uppercase;
  }

  .divider {
    position: absolute;
    left: 364px;
    top: 130px;
    width: 1px;
    height: 160px;
    background: var(--divider);
  }

  .contact {
    position: absolute;
    left: 385px;
    top: 126px;
    color: var(--text);
  }
  .contact-name {
    color: var(--accent);
    font-weight: 800;
    font-size: 21px;
    letter-spacing: 0.2px;
    text-transform: uppercase;
    line-height: 1.1;
  }
  .contact-title {
    color: var(--muted);
    font-weight: 700;
    font-size: 14.5px;
    text-transform: uppercase;
    line-height: 1.2;
    margin-top: 2px;
  }
  .contact-lines { margin-top: 14px; list-style: none; }
  .contact-lines li {
    display: flex;
    align-items: center;
    gap: 7px;
    font-size: 15.5px;
    line-height: 21px;
  }
  .contact-lines svg { width: 13px; height: 13px; fill: var(--accent); flex: none; }
  .address {
    margin-top: 9px;
    font-style: normal;
    font-size: 15.5px;
    line-height: 20.5px;
  }

  .tagline {
    position: absolute;
    left: 0; right: 0;
    top: 178px;
    text-align: center;
    font-weight: 700;
    font-size: 39px;
    line-height: 1;
  }
  .tagline-strong { color: var(--accent); }
  .tagline-soft { color: var(--muted); }
  .quote-mark {
    position: absolute;
    top: -14px;
    font-size: 62px;
    font-weight: 800;
    line-height: 1;
  }
  .quote-open { left: 68px; color: var(--accent); }
  .quote-close { left: 618px; color: var(--muted); }
</style>
</head>
<body>
  <section class="card card-front">
    <div class="brand">
      <span class="brand-dot"></span>
      <span class="brand-name">Responder<br>Training</span>
    </div>
    <div class="divider"></div>
    <div class="contact">
      <h1 class="contact-name">Daniel Whitmore</h1>
      <p class="contact-title">Managing Director</p>
      <ul class="contact-lines">
        <li>
          <svg viewBox="0 0 24 24" aria-hidden="true"><path d="M6.6 10.8a15.1 15.1 0 0 0 6.6 6.6l2.2-2.2c.3-.3.7-.4 1-.2 1.1.4 2.3.6 3.6.6.6 0 1 .4 1 1V20c0 .6-.4 1-1 1A17 17 0 0 1 3 4c0-.6.4-1 1-1h3.5c.6 0 1 .4 1 1 0 1.3.2 2.5.6 3.6.1.3 0 .7-.2 1z"/></svg>
          555 014 2630
        </li>
        <li>
          <svg viewBox="0 0 24 24" aria-hidden="true"><path d="M2 5h20v14H2z M2 5l10 8 10-8" /><path d="M2 5h20L12 12.5z" fill="#202a34"/></svg>
          info@respondertraining.com
        </li>
      </ul>
      <address class="address">
        118 Harbor Street<br>
        Suite 200, Norfolk<br>
        VA 23510
      </address>
    </div>
  </section>

  <section class="card card-back">
    <p class="tagline">
      <span class="quote-mark quote-open">&ldquo;</span>
      <span class="tagline-strong">We help you,</span>
      <span class="tagline-soft">help others</span>
      <span class="quote-mark quote-close">&rdquo;</span>
    </p>
  </section>
</body>
</html>
```